BROTH Nutrition Mobile Application Layout

I am looking for professional grade app page layouts to use in my clickable prototype for an investor pitch.

B.R.O.T.H. is an acronym for Balanced Routine Optimising Tailored Health.

This app is a nutrition diet generation tool for the consumer (type in profile, diet is generated).

I am most interested in several pages consisting of:
- A landing/login page
- User profile page which will consist of a visual representation of adherence to the diet such as a pie chart, bar with percentage representing said adherence, etc.
- Profile settings page
- Blank general layout page (a standard template to be used with all pages in the application)

I would prefer greens, reds, and yellows in the design
The design should reflect health and nutrition
The design should have an "ease of use appearance"

Apps that are useful to look at are:
Vitaltrack Buddy
Macroscope
Quickbasket

I have uploaded a "working" logo that I am using

I look forward to seeing your talents and appreciate your work in advance!

Target Market(s)

General population - health and wellness companies

Industry/Entity Type

Health And Wellness

Font styles to use
Serif
Sans Serif
Other font styles liked:
• Dealer's Choice

Colors
9ccb3b
f04a51
fbed22

Requirements
Must have
• - A landing/login page
• - User profile page which will consist of a visual representation of adherence to the diet such as a pie chart, bar with percentage representing said adherence, etc.
• - Profile settings page
• - Blank general layout page (a standard template to be used with all pages in the application)
• The design should reflect health and nutrition
• The design should have an "ease of use appearance"
Nice to have
• Incorporating the acronym spelled out.
• Common image in the background reflecting nutrition and health.

```html
<!DOCTYPE html>
<html lang="en">
<head>
<meta charset="utf-8">
<title>BROTH – Login</title>
<link href="https://fonts.googleapis.com/css2?family=Arimo:wght@400;700&display=swap" rel="stylesheet">
<style>
  :root {
    --page-bg: #f2f2f2;
    --screen-bg: #ffffff;
    --hero-dark: #2b211a;
    --hero-mid: #5a4232;
    --hero-warm: #7a5a40;
    --hero-overlay: rgba(20, 16, 12, 0.55);
    --text-light: #ffffff;
    --label: #6f6f6f;
    --field-border: #cfcfcf;
    --brand-green: #9ccb3b;
    --link: #555555;
  }
  * { box-sizing: border-box; margin: 0; padding: 0; }
  html, body {
    width: 1200px; height: 962px; overflow: hidden;
    background: var(--page-bg);
    font-family: "Arimo", Arial, sans-serif;
  }
  .screen {
    position: absolute; left: 347px; top: 31px;
    width: 506px; height: 900px;
    background: var(--screen-bg);
    overflow: hidden;
    box-shadow: 0 4px 24px rgba(0,0,0,0.12);
  }
  .hero {
    position: absolute; left: 0; top: 0; width: 100%; height: 486px;
    background:
      linear-gradient(var(--hero-overlay), var(--hero-overlay)),
      radial-gradient(ellipse at 70% 40%, var(--hero-warm) 0%, var(--hero-mid) 45%, var(--hero-dark) 100%);
  }
  .status-bar {
    position: absolute; left: 0; top: 0; width: 100%; height: 28px;
    display: flex; align-items: center; justify-content: space-between;
    padding: 0 10px; color: var(--text-light); font-size: 15px;
  }
  .status-left, .status-right { display: flex; align-items: center; gap: 6px; }
  .status-time { position: absolute; left: 50%; transform: translateX(-50%); font-weight: 700; }
  .brand-name {
    position: absolute; left: 0; top: 230px; width: 100%;
    text-align: center;
    color: var(--text-light); font-size: 34px; font-weight: 400; letter-spacing: 4px;
  }
  .login-form {
    position: absolute; left: 60px; right: 60px; top: 540px;
  }
  .field-row { display: flex; justify-content: space-between; align-items: baseline; }
  .field-label { color: var(--label); font-size: 23px; }
  .forgot-link { color: var(--link); font-size: 19px; text-decoration: none; }
  .field-input {
    display: block; width: 100%; height: 58px; margin: 8px 0 30px;
    border: 1px solid var(--field-border); background: var(--screen-bg);
  }
  .login-button {
    display: block; width: 100%; height: 50px; margin-top: 14px;
    border: none; background: var(--brand-green);
    color: var(--text-light); font-family: inherit; font-size: 23px; letter-spacing: 1px;
  }
</style>
</head>
<body>
  <main class="screen">
    <section class="hero" role="img" aria-label="Background photo of plated meals on a wooden table, darkened">
      <div class="status-bar">
        <div class="status-left">
          <svg width="52" height="10" viewBox="0 0 52 10" aria-hidden="true">
            <circle cx="5" cy="5" r="4" fill="#fff"/><circle cx="15" cy="5" r="4" fill="#fff"/>
            <circle cx="25" cy="5" r="4" fill="#fff"/><circle cx="35" cy="5" r="3.5" fill="none" stroke="#fff"/>
            <circle cx="45" cy="5" r="3.5" fill="none" stroke="#fff"/>
          </svg>
          <svg width="16" height="12" viewBox="0 0 16 12" aria-hidden="true">
            <path d="M1 4 A10 10 0 0 1 15 4" stroke="#fff" stroke-width="1.6" fill="none"/>
            <path d="M4 7 A6 6 0 0 1 12 7" stroke="#fff" stroke-width="1.6" fill="none"/>
            <circle cx="8" cy="10" r="1.6" fill="#fff"/>
          </svg>
        </div>
        <span class="status-time">4:21 PM</span>
        <div class="status-right">
          <svg width="8" height="14" viewBox="0 0 8 14" aria-hidden="true">
            <path d="M1 4 L7 10 L4 13 V1 L7 4 L1 10" stroke="#fff" stroke-width="1.2" fill="none"/>
          </svg>
          <span>80%</span>
          <svg width="30" height="13" viewBox="0 0 30 13" aria-hidden="true">
            <rect x="0.5" y="0.5" width="26" height="12" rx="2" fill="none" stroke="#fff"/>
            <rect x="2" y="2" width="19" height="9" fill="#fff"/>
            <rect x="27.5" y="4" width="2" height="5" fill="#fff"/>
          </svg>
        </div>
      </div>
      <span class="brand-name">BROTH</span>
    </section>

    <form class="login-form">
      <label class="field-label" for="email">Email</label>
      <input class="field-input" id="email" type="email">
      <div class="field-row">
        <label class="field-label" for="password">Password</label>
        <a class="forgot-link" href="#">Forget Password?</a>
      </div>
      <input class="field-input" id="password" type="password">
      <button class="login-button" type="button">LOGIN</button>
    </form>
  </main>
</body>
</html>
```